Business card for a shipping supplies business

Needing a business card design. Please see the logo. The logo with the white font should be used if there is a dark background.

We are looking for the following info on the card. Please see the sample info. We will need the info to be changed with a few different employee names and info but all will use the same template.

Business Name: The Crate Heron
Employee Name : Marcus Delaney
Position: Account Manager
Address: 4827 W. Ridge 418 S.
Fort Worth, TX 73948
email: Marcus@thecrateheron.example
telephone: 855-619-2740 x 207
website: www.getparcelkits.example

Target Market(s)

Businesses who ship products for online sales

Industry/Entity Type

Cardboard

Contact Information for Business Card

Name, title, address, website, logo, telephone number

Font styles to use
Sans Serif

Colors
EE7325
F08F49
F5BC92
FAE3D3
FDF4ED

Requirements
Must have
• Logo on back of card. Clean look, just logo, website address

```html
<!DOCTYPE html>
<html lang="en">
<head>
<meta charset="utf-8">
<title>The Crate Heron – Business Card</title>
<link href="https://fonts.googleapis.com/css2?family=Montserrat:wght@600;700&family=Mulish:wght@400;500&family=Open+Sans:wght@600&display=swap" rel="stylesheet">
<style>
  :root {
    --page: #ffffff;
    --card: #ffffff;
    --ink: #1b1b1b;
    --orange: #c9561f;
    --band: #7a2416;
    --tan: #b98a68;
    --white: #ffffff;
  }
  * { box-sizing: border-box; margin: 0; padding: 0; }
  html, body { width: 720px; height: 1200px; overflow: hidden; background: var(--page); }
  body { position: relative; font-family: "Mulish", sans-serif; color: var(--ink); }

  .card {
    position: absolute; left: 60px; width: 600px; height: 366px;
    background: var(--card);
    box-shadow: 0 6px 14px rgba(0,0,0,.28);
  }
  .card--front { top: 212px; }
  .card--back { top: 620px; }

  /* brand name */
  .brand {
    display: flex; align-items: center; gap: 12px;
    font-family: "Montserrat", sans-serif; font-weight: 700;
    color: var(--ink); white-space: nowrap;
  }
  .brand__mark { width: 14px; height: 14px; background: var(--orange); flex: none; }

  /* front */
  .card--front .brand {
    position: absolute; left: 0; right: 0; top: 150px;
    justify-content: center; font-size: 44px;
  }
  .front-web {
    position: absolute; left: 0; right: 0; top: 228px; text-align: center;
    font-size: 19px; letter-spacing: 2.4px; color: var(--ink);
  }

  /* back: identity side */
  .back-id { position: absolute; left: 0; top: 0; width: 303px; height: 366px; }
  .accent { position: absolute; left: 0; top: 52px; width: 18px; height: 20px; background: var(--tan); }
  .person__name {
    position: absolute; left: 34px; top: 46px;
    font-family: "Open Sans", sans-serif; font-weight: 600;
    font-size: 25px; line-height: 1; letter-spacing: -0.2px;
    color: var(--ink); white-space: nowrap;
  }
  .person__title {
    position: absolute; left: 34px; top: 80px;
    font-size: 16px; letter-spacing: .6px; color: var(--orange);
  }
  .card--back .brand {
    position: absolute; left: 24px; top: 265px; font-size: 24px; gap: 9px;
  }
  .card--back .brand__mark { width: 10px; height: 10px; }

  /* back: contact side */
  .contact-panel {
    position: absolute; left: 303px; top: 0; width: 297px; height: 366px;
    background: var(--orange);
  }
  .contact { position: absolute; left: 32px; display: flex; gap: 12px; color: var(--white); font-size: 14.5px; line-height: 1.45; white-space: nowrap; }
  .contact--phone { top: 50px; }
  .contact--address { top: 93px; }
  .contact--email { top: 157px; }
  .icon { width: 19px; height: 19px; flex: none; margin-top: 1px; }

  .web-band {
    position: absolute; left: 290px; top: 260px; width: 310px; height: 40px;
    background: var(--band); display: flex; align-items: center; gap: 10px;
    padding-left: 44px; color: var(--white); font-size: 17px; letter-spacing: .3px;
    white-space: nowrap;
  }
  .fold { position: absolute; left: 290px; width: 13px; height: 13px; }
  .fold--top { top: 247px; }
  .fold--bottom { top: 300px; }
</style>
</head>
<body>

<section class="card card--front" aria-label="Card front">
  <div class="brand"><span class="brand__mark"></span>The Crate Heron</div>
  <p class="front-web">www.getparcelkits.example</p>
</section>

<section class="card card--back" aria-label="Card back">
  <div class="back-id">
    <span class="accent"></span>
    <h1 class="person__name">MARCUS DELANEY</h1>
    <p class="person__title">ACCOUNT MANAGER</p>
    <div class="brand"><span class="brand__mark"></span>The Crate Heron</div>
  </div>

  <div class="contact-panel">
    <div class="contact contact--phone">
      <svg class="icon" viewBox="0 0 20 20"><rect width="20" height="20" fill="#7a2416"/><path d="M6 4.5l2 0 1 3-1.5 1a7 7 0 0 0 4 4l1-1.5 3 1 0 2c-6 .5-10-3.5-9.5-9.5z" fill="#fff"/></svg>
      <span>855-619-2740 x 207</span>
    </div>
    <div class="contact contact--address">
      <svg class="icon" viewBox="0 0 20 20"><rect width="20" height="20" fill="#7a2416"/><path d="M10 3.5a4.5 4.5 0 0 0-4.5 4.5c0 3.5 4.5 8.5 4.5 8.5s4.5-5 4.5-8.5A4.5 4.5 0 0 0 10 3.5z" fill="#fff"/><circle cx="10" cy="8" r="1.7" fill="#7a2416"/></svg>
      <span>4827 W. Ridge 418 S.<br>Fort Worth,TX 73948</span>
    </div>
    <div class="contact contact--email">
      <svg class="icon" viewBox="0 0 20 20"><rect width="20" height="20" fill="#7a2416"/><rect x="4.5" y="6" width="11" height="8" fill="#fff"/><path d="M4.5 6l5.5 4.5 5.5-4.5" fill="none" stroke="#7a2416" stroke-width="1.2"/></svg>
      <span>Marcus@thecrateheron.example</span>
    </div>
  </div>

  <svg class="fold fold--top" viewBox="0 0 13 13"><path d="M13 0V13H0z" fill="#7a2416"/></svg>
  <div class="web-band">
    <svg class="icon" viewBox="0 0 20 20" style="width:16px;height:16px"><circle cx="10" cy="10" r="7" fill="none" stroke="#fff" stroke-width="1.4"/><ellipse cx="10" cy="10" rx="3" ry="7" fill="none" stroke="#fff" stroke-width="1.2"/><path d="M3 10h14M4.5 6.5h11M4.5 13.5h11" stroke="#fff" stroke-width="1.1"/></svg>
    <span>www.getparcelkits.example</span>
  </div>
  <svg class="fold fold--bottom" viewBox="0 0 13 13"><path d="M0 0H13V13z" fill="#7a2416"/></svg>
</section>

</body>
</html>
```